Promotional Poster for "Skillets & Steins" Community Event

Skillets & Steins is a fun, high-energy annual fundraising event where guests enjoy gourmet taco creations and craft beer from some of Clark County's finest chefs and brewers. This community event is a fundraiser, supporting Harlow Basin Food Bank in Southwest Washington. We need a 11x17" full-color event poster for our 2019 Skillets & Steins event. For more information, visit our event website: www.skilletsandsteins.org
Target Market(s)
Poster to be displayed in breweries, restaurants, bars, and taprooms
Industry/Entity Type
Non Profit
Colors
Designer to choose colors to be used in the design.
Look and feel

```html
<!DOCTYPE html>
<html lang="en">
<head>
<meta charset="utf-8">
<title>Skillets &amp; Steins 2019 Poster</title>
<link rel="stylesheet" href="https://fonts.googleapis.com/css2?family=Saira+Condensed:wght@600;700&family=Saira+Semi+Condensed:wght@700&family=Libre+Baskerville:wght@700&display=swap">
<style>
  :root {
    --page: #ffffff;
    --poster-top: #7a7a7c;
    --poster-mid: #3b3b3d;
    --poster-bottom: #232325;
    --white: #ffffff;
    --band-light: #f4f4f2;
    --band-fade: #b9b9b9;
    --orange: #ec5a1f;
    --red-orange: #dc3b1e;
    --pill-red: #d3232f;
    --yellow: #f2c21b;
    --green: #1a8a4a;
    --rule: #d8d8d8;
  }
  * { margin: 0; padding: 0; box-sizing: border-box; }
  html, body { width: 923px; height: 1200px; overflow: hidden; background: var(--page); }
  .poster {
    position: absolute; left: 88px; top: 39px; width: 747px; height: 1122px; overflow: hidden;
    background: radial-gradient(ellipse 90% 55% at 50% 32%, var(--poster-top), var(--poster-mid) 60%, var(--poster-bottom));
    font-family: "Saira Condensed", sans-serif; color: var(--white); text-align: center;
  }
  .light-band {
    position: absolute; left: 231px; top: 0; width: 288px; height: 320px;
    background: linear-gradient(to bottom, var(--band-light) 0%, var(--band-light) 45%, var(--band-fade) 80%, transparent 100%);
  }
  .disco-ball { position: absolute; border-radius: 50%; }
  .disco-ball--left {
    left: -80px; top: -100px; width: 300px; height: 300px;
    background: radial-gradient(circle at 55% 60%, #c9a0a8, #8a4f5e 45%, #3d2a2e 80%);
  }
  .disco-ball--right {
    left: 572px; top: -40px; width: 320px; height: 320px;
    background: radial-gradient(circle at 40% 55%, #e8d59a, #a8883a 45%, #4a6a6e 85%);
  }
  .host {
    position: absolute; left: 231px; top: 140px; width: 288px;
    display: flex; align-items: center; justify-content: center; gap: 10px;
  }
  .host-mark { width: 30px; height: 30px; border-radius: 50%; background: var(--green); flex: none; }
  .host-name {
    font-family: "Libre Baskerville", serif; font-weight: 700; font-size: 17px; line-height: 1.15;
    color: var(--green); text-align: left; width: 160px;
  }
  .event-badge { position: absolute; left: 226px; top: 210px; width: 296px; height: 296px; }
  .event-name {
    position: absolute; left: 226px; top: 210px; width: 296px; height: 296px;
    display: flex; align-items: center; justify-content: center;
    font-weight: 700; font-size: 56px; line-height: 0.95; color: #1b1b1b;
  }
  .line { position: absolute; left: 0; width: 100%; white-space: nowrap; }
  .dates { font-weight: 700; font-size: 42px; line-height: 1; }
  .date-1 { top: 524px; }
  .date-2 { top: 575px; }
  .rule { position: absolute; left: 0; width: 100%; height: 2px; background: var(--rule); }
  .rule--top { top: 628px; }
  .rule--bottom { top: 784px; }
  .tickets { font-weight: 700; font-size: 35px; line-height: 1; font-variant: small-caps; letter-spacing: 0.5px; }
  .ticket-ga { top: 644px; color: var(--orange); }
  .ticket-vip { top: 681px; color: var(--orange); }
  .ticket-six { top: 722px; color: var(--red-orange); }
  .site-pill {
    position: absolute; left: 212px; top: 766px; width: 323px; height: 35px; border-radius: 9px;
    background: var(--pill-red); font-weight: 700; font-size: 22px; line-height: 35px;
  }
  .featuring-label { top: 816px; color: var(--yellow); font-weight: 700; font-size: 20px; font-variant: small-caps; }
  .features { position: absolute; left: 0; top: 842px; width: 100%; list-style: none; }
  .features li {
    font-family: "Saira Semi Condensed", sans-serif; font-weight: 700; font-size: 31px;
    line-height: 34px; font-variant: small-caps; letter-spacing: 1px;
  }
</style>
</head>
<body>
<main class="poster">
  <div class="disco-ball disco-ball--left" role="img" aria-label="Rose-coloured mirrored disco ball"></div>
  <div class="disco-ball disco-ball--right" role="img" aria-label="Gold mirrored disco ball"></div>
  <div class="light-band"></div>

  <div class="host">
    <span class="host-mark"></span>
    <span class="host-name">Harlow Basin Food Bank</span>
  </div>

  <svg class="event-badge" viewBox="0 0 296 296" aria-hidden="true">
    <defs>
      <radialGradient id="badgeFill" cx="50%" cy="45%" r="60%">
        <stop offset="0" stop-color="#f4f4f4"/>
        <stop offset="0.7" stop-color="#bdbdbd"/>
        <stop offset="1" stop-color="#8c8c8c"/>
      </radialGradient>
    </defs>
    <circle cx="148" cy="148" r="146" fill="#d9d9d9"/>
    <circle cx="148" cy="148" r="136" fill="url(#badgeFill)"/>
  </svg>
  <div class="event-name">Skillets<br>&amp; Steins</div>

  <div class="line dates date-1">Friday, May 3, 2019</div>
  <div class="line dates date-2">Saturday, May 4, 2019</div>

  <div class="rule rule--top"></div>
  <div class="line tickets ticket-ga">General Admission: $35</div>
  <div class="line tickets ticket-vip">VIP Fiesta Ticket: $45</div>
  <div class="line tickets ticket-six">6-Pack Tickets Available</div>
  <div class="rule rule--bottom"></div>
  <div class="site-pill">WWW.SKILLETSANDSTEINS.ORG</div>

  <div class="line featuring-label">Featuring:</div>
  <ul class="features">
    <li>12 Breweries</li>
    <li>12 Restaurants</li>
    <li>Desserts &amp; Beverages</li>
    <li>Raffle Drawing</li>
    <li>Live Music</li>
    <li>Beer Bottle Ring Toss</li>
  </ul>
</main>
</body>
</html>
```